!st birthday celebration

Im looking for a celebration type of flyer for our first birthday. something colorful and eye catching but with a vintage feel to it. we are a vintage shop with a friendly atmosphere and always have music playing. I have attached a draft copy i have been working on so far. Thanks

Industry/Entity Type

Shop

```html
<!DOCTYPE html>
<html lang="en">
<head>
<meta charset="utf-8">
<title>2208 Vintage – Happy 1st Birthday</title>
<link rel="stylesheet" href="https://fonts.googleapis.com/css2?family=Oswald:wght@400;500;600&display=swap">
<style>
  :root {
    --orange: #ee6a2b;
    --orange-deep: #e2532a;
    --brick: #b7461f;
    --yellow: #fbb83f;
    --cream: #fff7dc;
    --white: #ffffff;
    --text: #e2502a;
  }
  * { margin: 0; padding: 0; box-sizing: border-box; }
  html, body { width: 848px; height: 1200px; overflow: hidden; background: var(--orange); }
  .flyer {
    position: relative;
    width: 848px;
    height: 1200px;
    overflow: hidden;
    background: radial-gradient(circle at 50% 50%, #f7923a 0%, var(--orange) 55%, #e4552a 100%);
    border: 8px solid var(--brick);
    font-family: "Oswald", sans-serif;
    color: var(--text);
    text-transform: uppercase;
  }
  .shop-name {
    position: absolute;
    top: 68px; left: 0; width: 100%;
    text-align: center;
    font-weight: 600;
    font-size: 58px;
    line-height: 1;
    text-transform: none;
    color: var(--white);
    letter-spacing: 1px;
    white-space: nowrap;
  }
  .ribbons { position: absolute; left: 0; top: 0; }
  .panel {
    position: absolute;
    left: 91px; top: 305px;
    width: 662px; height: 720px;
    background: radial-gradient(circle at 50% 42%, #ffffff 0%, var(--cream) 45%, #fde3a4 100%);
  }
  .panel-edge {
    position: absolute;
    top: 0; width: 104px; height: 100%;
    background: linear-gradient(180deg, var(--brick), var(--orange-deep) 30%, var(--yellow) 50%, var(--orange-deep) 70%, var(--brick));
  }
  .panel-edge.left { left: 0; }
  .panel-edge.right { right: 0; }
  .banner-text {
    position: absolute;
    left: 0; width: 100%;
    text-align: center;
    font-weight: 500;
    font-size: 68px;
    line-height: 1;
    color: var(--text);
    letter-spacing: 3px;
    white-space: nowrap;
  }
  .banner-text.top { top: 218px; }
  .banner-text.bottom { top: 1041px; }
  .content { position: absolute; left: 0; width: 100%; text-align: center; white-space: nowrap; }
  .invite { top: 330px; font-size: 21px; line-height: 28px; }
  .date { top: 418px; font-size: 21px; line-height: 28px; }
  .rule { position: absolute; height: 3px; background: var(--brick); }
  .rule.one { left: 276px; width: 303px; top: 400px; }
  .rule.two { left: 209px; width: 438px; top: 488px; }
  .rule.three { left: 245px; width: 370px; top: 872px; }
  .festivities-label { top: 508px; font-size: 12px; line-height: 16px; letter-spacing: 1px; }
  .festivities {
    top: 536px;
    list-style: none;
    font-weight: 500;
    font-size: 31px;
    line-height: 40px;
  }
  .festivities .star { color: var(--yellow); font-size: 20px; vertical-align: 5px; padding: 0 4px; }
  .address { top: 886px; font-size: 17px; line-height: 28px; }
  .phone-big { top: 938px; font-size: 48px; line-height: 60px; font-weight: 500; letter-spacing: 1px; }
</style>
</head>
<body>
<main class="flyer">
  <div class="shop-name">2208 Vintage</div>

  <div class="panel">
    <div class="panel-edge left" role="img" aria-label="Column of retro concentric rings in brick, orange and yellow"></div>
    <div class="panel-edge right" role="img" aria-label="Column of retro concentric rings in brick, orange and yellow"></div>
  </div>

  <svg class="ribbons" width="848" height="1200" viewBox="0 0 848 1200" aria-hidden="true">
    <polygon points="10,232 100,232 100,338 10,338 42,285" fill="var(--brick)"/>
    <polygon points="18,242 94,242 94,328 18,328 48,285" fill="var(--white)" stroke="var(--yellow)" stroke-width="5"/>
    <polygon points="838,232 748,232 748,338 838,338 806,285" fill="var(--brick)"/>
    <polygon points="830,242 754,242 754,328 830,328 800,285" fill="var(--white)" stroke="var(--yellow)" stroke-width="5"/>
    <rect x="62" y="190" width="724" height="128" fill="var(--brick)"/>
    <rect x="70" y="198" width="708" height="112" fill="var(--white)"/>
    <rect x="78" y="206" width="692" height="96" fill="none" stroke="var(--yellow)" stroke-width="4"/>
    <polygon points="10,990 100,990 100,1096 10,1096 42,1043" fill="var(--brick)"/>
    <polygon points="18,1000 94,1000 94,1086 18,1086 48,1043" fill="var(--white)" stroke="var(--yellow)" stroke-width="5"/>
    <polygon points="838,990 748,990 748,1096 838,1096 806,1043" fill="var(--brick)"/>
    <polygon points="830,1000 754,1000 754,1086 830,1086 800,1043" fill="var(--white)" stroke="var(--yellow)" stroke-width="5"/>
    <rect x="62" y="1014" width="724" height="126" fill="var(--brick)"/>
    <rect x="70" y="1022" width="708" height="110" fill="var(--white)"/>
    <rect x="78" y="1030" width="692" height="94" fill="none" stroke="var(--yellow)" stroke-width="4"/>
  </svg>

  <h1 class="banner-text top">Happy 1st Birthday</h1>

  <p class="content invite">You are invited to help<br>celebrate in the festivities!</p>
  <div class="rule one"></div>
  <p class="content date">19th &amp; 20th July 2014<br>Starting from 11am onwards</p>
  <div class="rule two"></div>
  <p class="content festivities-label">- Festivities include -</p>
  <ul class="content festivities">
    <li><span class="star">★</span>Pop-up market stalls<span class="star">★</span></li>
    <li><span class="star">★</span>Best dressed vintage outfit<span class="star">★</span></li>
    <li><span class="star">★</span>Face painting<span class="star">★</span></li>
    <li><span class="star">★</span>Vintage cars on display<span class="star">★</span></li>
    <li><span class="star">★</span>Music<span class="star">★</span></li>
    <li><span class="star">★</span>Refreshments<span class="star">★</span></li>
    <li><span class="star">★</span>Psychic readings<span class="star">★</span></li>
    <li>+More!</li>
  </ul>
  <div class="rule three"></div>
  <p class="content address">2208 Harbour Ridge Rd, Kelby<br>Ph: 55 018</p>
  <p class="content phone-big">0491570110</p>

  <h2 class="banner-text bottom">2208 Vintage!</h2>
</main>
</body>
</html>
```